Yoga Workshop - Yoga Practice information flyer

I am a yoga teacher who will be presenting a workshop on yoga for sleep and need a brochure for my clients which outlines a practice that I give them so they can do the practice at home. Ideally I would like a brochure that is a single A3 size of paper in size that folds in half to an A4 booklet with the entire practice on the centre section to make it easy for people to do the practice at home with just one open page in front of them:
* Front page detailing "Yoga for Sleep Workshop" and "Restorative Yoga Practice"
* Centre contains the information on the practice contained in the attached word document. The practice consists of 5 postures, so there needs to be five separate sections which have the pictures of the postures (attached in uploaded files) and the wording contained in the attached word document. All pictures uploaded need to be included in the flyer as each posture has different pictures demonstrating the posture using yoga props or using things people have at home
* Back page containing a picture of myself (picture uploaded in files) with some information about me (contained in the attached word document) and my website www.lunavesperflow.com.au

I also need this flyer to be able to printed on 2 double sided A4 sheets of paper so will require 2 x pdf file versions. Importantly, for the centre section of the flyer, the design needs to ensure if it is printed on A4 paper, the wording and pictures for each of the postures are not separated over two pages

Target Market(s)

Existing clients

Requirements
Must have
• Detailed in project description
Nice to have
• The word document also contains some quotes. These do not need to be included in the flyer. If there is room and there is room for one or two of those please include where it would look good
Should not have
• Stock pictures of people in yoga postures which a normal everyday person could not get into

```html
<!DOCTYPE html>
<html lang="en">
<head>
<meta charset="utf-8">
<title>Yoga for Sleep Workshop – Brochure</title>
<link href="https://fonts.googleapis.com/css2?family=Playfair+Display:wght@700;900&family=Open+Sans:wght@400;600;700&display=swap" rel="stylesheet">
<style>
:root{
  --clay:#c47a4f;
  --clay-dark:#a65f38;
  --clay-soft:#e9c7b0;
  --ink:#2f2f2f;
  --muted:#6b6b6b;
  --paper:#ffffff;
  --stage:#ecebe9;
  --rule:#d9d4cf;
}
*{box-sizing:border-box;margin:0;padding:0}
html,body{width:1200px;height:3100px;overflow:hidden;background:var(--stage);font-family:"Open Sans",Arial,sans-serif;color:var(--ink)}
.spread{position:absolute;left:30px;width:1140px;height:806px;background:var(--paper);box-shadow:0 4px 18px rgba(0,0,0,.12);overflow:hidden}
.spread--outer{top:430px}
.spread--inner{top:1760px}
.fold{position:absolute;left:570px;top:0;width:1px;height:100%;background:rgba(0,0,0,.06)}
.photo{position:absolute}

/* outer spread */
.brand{position:absolute;left:570px;width:570px;top:42px;text-align:center}
.brand__name{display:inline-flex;align-items:center;gap:10px;font-family:"Open Sans",Arial,sans-serif;font-weight:700;font-size:26px;color:var(--clay)}
.brand__dot{width:14px;height:14px;border-radius:50%;background:var(--clay)}
.brand__tagline{font-size:11px;color:var(--muted);margin-top:8px;font-style:normal}
.header-rule{position:absolute;left:0;top:150px;width:100%;height:4px;background:var(--clay)}
.about{position:absolute;left:340px;top:175px;width:290px;height:325px;background:var(--clay);color:#fff;padding:28px 26px}
.about__title{font-family:"Open Sans",Arial,sans-serif;font-weight:700;font-size:17px;line-height:1.2;letter-spacing:.5px}
.about__title::after{content:"";display:block;width:46px;height:2px;background:#fff;margin:10px 0 14px}
.about__text{font-size:10.5px;line-height:1.55}
.about__text+.about__text{margin-top:8px}
.title-block{position:absolute;left:640px;top:535px;width:470px;text-align:right}
.title-block__line1{font-family:"Playfair Display",Georgia,serif;font-weight:900;font-size:54px;line-height:1;color:var(--clay)}
.title-block__line2{font-family:"Playfair Display",Georgia,serif;font-weight:900;font-size:46px;line-height:1.1;color:var(--clay-dark)}
.title-block__line3{font-family:"Playfair Display",Georgia,serif;font-weight:700;font-size:27px;color:var(--clay);margin-top:6px;letter-spacing:.5px}
.title-block__web{font-size:19px;font-weight:700;color:var(--ink);margin-top:14px;letter-spacing:.5px}
.contact{position:absolute;left:55px;top:580px;display:flex;flex-wrap:wrap;gap:12px 26px;width:470px;font-size:11px;color:var(--muted)}
.contact__item{display:flex;align-items:center;gap:7px}
.contact__item svg{width:16px;height:16px;fill:var(--clay)}
.back-brand{position:absolute;left:55px;top:720px;display:flex;align-items:center;gap:8px;font-weight:700;font-size:15px;color:var(--clay)}
.back-brand__dot{width:10px;height:10px;border-radius:50%;background:var(--clay)}

/* inner spread */
.sequence-title{position:absolute;left:32px;top:28px;font-family:"Playfair Display",Georgia,serif;font-weight:700;font-size:22px;color:var(--clay-dark)}
.intro{position:absolute;left:32px;top:66px;width:510px;font-size:10px;line-height:1.55;color:var(--muted)}
.posture{position:absolute;width:515px}
.posture__photos{position:absolute;left:0;top:0;display:flex;gap:6px}
.posture__photos .ph{width:110px;height:160px}
.posture__body{position:absolute;top:0}
.posture__num{font-size:11px;font-weight:700;color:var(--clay)}
.posture__name{display:block;background:var(--clay);color:#fff;font-weight:700;font-size:12px;padding:5px 10px;margin:3px 0 8px}
.posture__label{font-size:10px;font-weight:700;color:var(--ink);margin-top:5px}
.posture__text{font-size:9.5px;line-height:1.5;color:var(--muted)}
.testimonials{position:absolute;left:640px;top:505px;width:470px;height:250px;background:#f4efeb;border-top:4px solid var(--clay);padding:22px 28px}
.testimonials__title{font-family:"Playfair Display",Georgia,serif;font-weight:700;font-size:20px;color:var(--ink);text-align:center;letter-spacing:1px}
.testimonials__mark{font-family:"Playfair Display",Georgia,serif;font-size:48px;line-height:.6;color:var(--clay);margin-top:14px}
.testimonials__quote{font-size:12px;line-height:1.65;color:var(--ink);padding-left:26px}
.testimonials__cite{text-align:right;font-size:12px;font-weight:700;color:var(--clay);margin-top:6px}
.page-brand{position:absolute;left:1000px;top:770px;display:flex;align-items:center;gap:7px;font-weight:700;font-size:12px;color:var(--clay)}
.page-brand__dot{width:8px;height:8px;border-radius:50%;background:var(--clay)}
.footer-tab{position:absolute;left:32px;top:776px;width:40px;height:8px;background:var(--clay)}
</style>
</head>
<body>

<section class="spread spread--outer">
  <div class="fold"></div>

  <div class="brand">
    <div class="brand__name"><span class="brand__dot"></span>Luna Vesper Flow</div>
    <p class="brand__tagline">We can change our life when we change our mind</p>
  </div>
  <div class="header-rule"></div>

  <div class="photo" style="left:55px;top:175px;width:285px;height:325px;background:linear-gradient(160deg,#7d9a5a,#b9c79a 55%,#8a8f86)" role="img" aria-label="Photo of the teacher sitting cross-legged on grass in a garden"></div>
  <div class="about">
    <h2 class="about__title">ABOUT<br>THE TEACHER...</h2>
    <p class="about__text">I have taught yoga for many years and love helping people find ease, rest and calm in body and mind through gentle practice.</p>
    <p class="about__text">My classes blend restorative postures, breath and stillness so each student can build a simple home practice that supports deep and restful sleep.</p>
  </div>
  <div class="photo" style="left:630px;top:175px;width:510px;height:325px;background:linear-gradient(180deg,#e8e3dd,#d6cfc6)" role="img" aria-label="Photo of a woman seated in meditation, seen from behind"></div>

  <div class="title-block">
    <div class="title-block__line1">YOGA FOR</div>
    <div class="title-block__line2">SLEEP WORKSHOP</div>
    <div class="title-block__line3">RESTORATIVE YOGA PRACTICE</div>
    <div class="title-block__web">www.lunavesperflow.com.au</div>
  </div>

  <div class="contact">
    <div class="contact__item"><svg viewBox="0 0 24 24"><path d="M12 2a7 7 0 0 0-7 7c0 5 7 13 7 13s7-8 7-13a7 7 0 0 0-7-7zm0 9.5A2.5 2.5 0 1 1 12 6.5a2.5 2.5 0 0 1 0 5z"/></svg>PO Box 417, Tidewater NSW 2999</div>
    <div class="contact__item"><svg viewBox="0 0 24 24"><path d="M3 5h18v14H3z" fill="none" stroke="#c47a4f" stroke-width="2"/><path d="M3 6l9 7 9-7" fill="none" stroke="#c47a4f" stroke-width="2"/></svg>hello@lunavesperflow.com.au</div>
    <div class="contact__item"><svg viewBox="0 0 24 24"><circle cx="12" cy="12" r="9" fill="none" stroke="#c47a4f" stroke-width="2"/><path d="M3 12h18M12 3c3 3 3 15 0 18M12 3c-3 3-3 15 0 18" fill="none" stroke="#c47a4f" stroke-width="1.5"/></svg>www.lunavesperflow.com.au</div>
  </div>
  <div class="back-brand"><span class="back-brand__dot"></span>Luna Vesper Flow</div>
</section>

<section class="spread spread--inner">
  <div class="fold"></div>

  <h2 class="sequence-title">Restorative Yoga Sleep Sequence</h2>
  <p class="intro">This gentle sequence is designed to calm the nervous system before bed. Move slowly, breathe softly through the nose and stay in each posture for five to ten minutes. Use yoga props or simple items from home such as pillows, blankets and a chair. Rest in each shape without effort and let the body grow heavy.</p>

  <article class="posture" style="left:32px;top:150px">
    <div class="posture__photos">
      <div class="ph" style="background:linear-gradient(160deg,#c9b59c,#5d7fa8)" role="img" aria-label="Photo of posture one with a bolster"></div>
      <div class="ph" style="background:linear-gradient(160deg,#d2c2ac,#7a6a8c)" role="img" aria-label="Photo of posture one with home pillows"></div>
    </div>
    <div class="posture__body" style="left:240px;width:275px">
      <div class="posture__num">Posture 1</div>
      <span class="posture__name">Supported Child's Pose</span>
      <div class="posture__label">Props:</div>
      <p class="posture__text">Bolster or two firm pillows, a folded blanket.</p>
      <div class="posture__label">Instructions:</div>
      <p class="posture__text">Kneel with knees wide, rest your chest and head on the bolster and let your arms relax.</p>
    </div>
  </article>

  <article class="posture" style="left:32px;top:360px">
    <div class="posture__photos">
      <div class="ph" style="background:linear-gradient(160deg,#c8a98e,#b04a5a)" role="img" aria-label="Photo of posture two with a yoga block"></div>
      <div class="ph" style="background:linear-gradient(160deg,#cdb8a1,#4f77a6)" role="img" aria-label="Photo of posture two with a cushion"></div>
    </div>
    <div class="posture__body" style="left:240px;width:275px">
      <div class="posture__num">Posture 2</div>
      <span class="posture__name">Supported Bridge Pose</span>
      <div class="posture__label">Props:</div>
      <p class="posture__text">Yoga block or a firm cushion.</p>
      <div class="posture__label">Instructions:</div>
      <p class="posture__text">Lie on your back, lift the hips and slide the block under your sacrum. Rest fully on it.</p>
    </div>
  </article>

  <article class="posture" style="left:32px;top:570px">
    <div class="posture__photos">
      <div class="ph" style="background:linear-gradient(180deg,#d9d2c8,#6a86a8)" role="img" aria-label="Photo of posture three with legs resting on a wall"></div>
      <div class="ph" style="background:linear-gradient(180deg,#d4c9bb,#8a6f5d)" role="img" aria-label="Photo of posture three with legs on a chair"></div>
    </div>
    <div class="posture__body" style="left:240px;width:275px">
      <div class="posture__num">Posture 3</div>
      <span class="posture__name">Legs Up the Wall</span>
      <div class="posture__label">Props:</div>
      <p class="posture__text">A wall or chair, a folded blanket.</p>
      <div class="posture__label">Instructions:</div>
      <p class="posture__text">Lie near the wall and rest your legs up it. Let the back soften into the floor.</p>
    </div>
  </article>

  <article class="posture" style="left:600px;top:40px">
    <div class="posture__body" style="left:0;width:270px">
      <div class="posture__num">Posture 4</div>
      <span class="posture__name">Reclined Bound Angle</span>
      <div class="posture__label">Props:</div>
      <p class="posture__text">Bolster, two blocks or pillows under the knees.</p>
      <div class="posture__label">Instructions:</div>
      <p class="posture__text">Recline on the bolster, soles together, knees resting on the props at each side.</p>
    </div>
    <div class="photo" style="left:290px;top:10px;width:220px;height:170px;background:linear-gradient(160deg,#c7b49e,#5a7ca6)" role="img" aria-label="Photos of posture four reclining on a bolster"></div>
  </article>

  <article class="posture" style="left:600px;top:270px">
    <div class="posture__body" style="left:0;width:270px">
      <div class="posture__num">Posture 5</div>
      <span class="posture__name">Supported Savasana</span>
      <div class="posture__label">Props:</div>
      <p class="posture__text">Pillow under knees, blanket for warmth, eye pillow.</p>
      <div class="posture__label">Instructions:</div>
      <p class="posture__text">Lie on your back, cover yourself and let the whole body rest in stillness.</p>
    </div>
    <div class="photo" style="left:290px;top:10px;width:220px;height:170px;background:linear-gradient(160deg,#cbbaa6,#9b5a4c)" role="img" aria-label="Photos of posture five resting on the back under a blanket"></div>
  </article>

  <aside class="testimonials">
    <h3 class="testimonials__title">TESTIMONIALS</h3>
    <div class="testimonials__mark">&ldquo;</div>
    <p class="testimonials__quote">Watch your thoughts, they become words.<br>Watch your words, they become actions.<br>Watch your actions, they become habit.<br>Watch your habits, they become character.<br>Watch your character, for it becomes your destiny.</p>
    <p class="testimonials__cite">~ Upanishads</p>
  </aside>

  <div class="footer-tab"></div>
  <div class="page-brand"><span class="page-brand__dot"></span>Luna Vesper Flow</div>
</section>

</body>
</html>
```